pressure washing advertisment

I would like front and back designed post cards. we offer pressure washing services for residential customers. I want to highlight before and after pictures as examples of our more popular services. I would also like to have our email www.bluhavenwashco.example and the facebook and Instagram logo somewhere. you can also include all major credit card logos as acceptable payments. I have attached our logo along with before and after pictures. also feel free to go to my website for any additional information that should be added to the post card. lastly I want a small promotion of $25 off any service somewhere.<br/><br/>Thank you!!

Target Market(s)

homeowners

Industry/Entity Type

Cleaning Service

Font styles to use
Serif
Sans Serif

Colors

Designer to choose colors to be used in the design.

Requirements
Must have
• before and after pictures with website and logo
Nice to have
• clean look that flows

```html
<!DOCTYPE html>
<html lang="en">
<head>
<meta charset="utf-8">
<title>Bluhaven Wash Co – Postcard</title>
<link href="https://fonts.googleapis.com/css2?family=Source+Serif+4:ital,opsz,wght@0,8..60,400;0,8..60,700;0,8..60,800;1,8..60,400;1,8..60,700&family=Arimo:ital@1&display=swap" rel="stylesheet">
<style>
  :root{
    --page:#34373a;
    --card:#f2f2f2;
    --sky:#2b86d9;
    --sky-soft:#3a8fd8;
    --navy:#1a35a8;
    --ink:#222;
    --deal-a:#f0457f;
    --deal-b:#e4001c;
    --white:#ffffff;
  }
  *{box-sizing:border-box;margin:0;padding:0}
  html,body{width:1200px;height:1200px;overflow:hidden;background:var(--page)}
  body{position:relative;font-family:"Source Serif 4",Georgia,serif}
  .card{position:absolute;left:230px;width:740px;height:493px;background:var(--card);box-shadow:0 6px 18px rgba(0,0,0,.45)}
  .card--front{top:102px}
  .card--back{top:630px}
  .abs{position:absolute}

  /* front */
  .kicker{left:0;width:566px;top:58px;text-align:center;font-family:"Arimo",Arial,sans-serif;font-style:italic;font-size:30px;color:var(--navy);letter-spacing:1px}
  .kicker span{text-decoration:underline;text-decoration-thickness:2px;text-underline-offset:3px}
  .headline{left:0;width:566px;text-align:center;color:var(--sky);font-weight:800;line-height:1}
  .headline--one{top:72px;font-size:94px;letter-spacing:-1px}
  .headline--two{top:155px;font-size:100px;letter-spacing:-1px}
  .services-band{left:146px;top:245px;width:274px;height:57px;background:var(--sky);color:var(--white);font-weight:800;font-size:50px;line-height:57px;text-align:center}
  .brand{display:flex;align-items:center;gap:7px;font-weight:700;color:var(--navy);white-space:nowrap}
  .brand__mark{width:12px;height:12px;background:var(--deal-b)}
  .brand--front{left:552px;top:62px;font-size:19px}
  .deal{left:587px;top:195px;width:122px;height:122px;border-radius:50%;background:linear-gradient(160deg,var(--deal-a),var(--deal-b) 75%);color:var(--white);text-align:center;font-weight:700;line-height:1}
  .deal__amount{display:block;margin-top:28px;font-size:36px}
  .deal__label{display:block;font-style:italic;font-weight:400;font-size:36px;margin-top:2px}
  .tile{top:347px;width:164px;height:91px;background:var(--white);padding:3px;display:flex;gap:3px}
  .tile__half{flex:1}
  .caption{top:444px;width:164px;text-align:center;color:var(--sky-soft);font-size:13.5px;line-height:16px}
  .t1{left:27px}.t2{left:201px}.t3{left:375px}.t4{left:549px}
  .house-before{background:linear-gradient(180deg,#7db1e2,#d8c88f 45%,#c9b878 80%,#4b6a34)}
  .house-after{background:linear-gradient(180deg,#5f9ee0,#e6d79f 45%,#d8c98c 80%,#4e7038)}
  .gutter-before{background:linear-gradient(180deg,#cfc9bd,#b27a44 55%,#5d8d35 70%,#3f6e27)}
  .gutter-after{background:linear-gradient(180deg,#e4e4e2,#d7d7d5 60%,#6a9c3c 70%,#3f6e27)}
  .drive-before{background:linear-gradient(180deg,#2d3a26,#5b6452 30%,#b9b7b0 45%,#a3a09a)}
  .drive-after{background:linear-gradient(180deg,#2d3a26,#5b6452 30%,#cfcfcc 45%,#c2c2bf)}
  .fence-before{background:linear-gradient(180deg,#5d8fd0,#6c7175 35%,#c8c8c6 60%,#9a9b9c)}
  .fence-after{background:linear-gradient(180deg,#4b86d2,#7c8185 35%,#e2e2e0 60%,#b3b4b4)}

  /* back */
  .brand--back{left:37px;top:60px;font-size:19px}
  .stamp-box{left:609px;top:55px;width:79px;height:89px;border:1px solid var(--ink)}
  .address-line{left:388px;width:300px;height:0;border-top:1.3px solid var(--ink)}
  .cta{left:34px;top:150px;width:300px;font-style:italic;font-weight:700;color:var(--navy);font-size:31px;line-height:37px}
  .contact{left:37px;top:285px;list-style:none}
  .contact li{display:flex;align-items:center;gap:7px;height:26.5px;font-style:italic;font-size:10.5px;color:var(--navy)}
  .contact__icon{width:22px;height:22px;flex:none}
  .payment-label{left:42px;top:422px;font-style:italic;font-size:11px;color:var(--navy)}
  .payment-row{left:42px;top:441px;display:flex;gap:3px}
  .pay-chip{width:21px;height:14px;border-radius:1px}
  .chip-a{background:#2f6fd6}.chip-b{background:#e9eef7}.chip-c{background:#d9ecf5}
  .chip-d{background:#e7e9ee}.chip-e{background:#2f3650}.chip-f{background:#3aa0e6}.chip-g{background:#eeeeee}
</style>
</head>
<body>

<section class="card card--front" aria-label="Postcard front">
  <p class="abs kicker"><span>Residential</span></p>
  <h1 class="abs headline headline--one">Pressure</h1>
  <p class="abs headline headline--two">Washing</p>
  <p class="abs services-band">services</p>

  <div class="abs brand brand--front"><span class="brand__mark"></span>Bluhaven Wash Co</div>

  <div class="abs deal"><span class="deal__amount">25$</span><span class="deal__label">OFF</span></div>

  <div class="abs tile t1">
    <div class="tile__half house-before" role="img" aria-label="House siding before soft washing"></div>
    <div class="tile__half house-after" role="img" aria-label="House siding after soft washing"></div>
  </div>
  <p class="abs caption t1">Soft Wash House<br>Washing</p>

  <div class="abs tile t2">
    <div class="tile__half gutter-before" role="img" aria-label="Stained wall base before cleaning"></div>
    <div class="tile__half gutter-after" role="img" aria-label="Wall base after brightening"></div>
  </div>
  <p class="abs caption t2">Gutter Cleaning &amp;<br>Brightening</p>

  <div class="abs tile t3">
    <div class="tile__half drive-before" role="img" aria-label="Driveway before concrete cleaning"></div>
    <div class="tile__half drive-after" role="img" aria-label="Driveway after concrete cleaning"></div>
  </div>
  <p class="abs caption t3">Driveway &amp;<br>Concrete Cleaning</p>

  <div class="abs tile t4">
    <div class="tile__half fence-before" role="img" aria-label="Home exterior before cleaning"></div>
    <div class="tile__half fence-after" role="img" aria-label="Home exterior after cleaning"></div>
  </div>
  <p class="abs caption t4">Deck &amp; Fence<br>Cleaning</p>
</section>

<section class="card card--back" aria-label="Postcard back">
  <div class="abs brand brand--back"><span class="brand__mark"></span>Bluhaven Wash Co</div>
  <div class="abs stamp-box"></div>

  <p class="abs cta">Contact us today to schedule your next cleaning service.</p>

  <ul class="abs contact">
    <li>
      <svg class="contact__icon" viewBox="0 0 22 22"><circle cx="11" cy="11" r="11" fill="#2b86d9"/><path d="M7.5 5.5l2 .3.8 2.6-1.3 1.1c.7 1.5 1.8 2.6 3.3 3.3l1.1-1.3 2.6.8.3 2c-.2.6-.9 1-1.6 1C10 15.3 6.7 12 6.5 7.3c0-.8.4-1.5 1-1.8z" fill="#fff"/></svg>
      (555) 014-2290
    </li>
    <li>
      <svg class="contact__icon" viewBox="0 0 22 22"><circle cx="11" cy="11" r="11" fill="#2b86d9"/><g fill="none" stroke="#fff" stroke-width="1.1"><circle cx="11" cy="11" r="5.5"/><ellipse cx="11" cy="11" rx="2.4" ry="5.5"/><path d="M5.5 11h11M6.3 8.2h9.4M6.3 13.8h9.4"/></g></svg>
      www.bluhavenwashco.example
    </li>
    <li>
      <svg class="contact__icon" viewBox="0 0 22 22"><circle cx="11" cy="11" r="11" fill="#2b86d9"/></svg>
      photos/bluhavenwashco
    </li>
    <li>
      <svg class="contact__icon" viewBox="0 0 22 22"><circle cx="11" cy="11" r="11" fill="#2b86d9"/></svg>
      community/BluhavenWashCo
    </li>
  </ul>

  <div class="abs address-line" style="top:196px"></div>
  <div class="abs address-line" style="top:247px"></div>
  <div class="abs address-line" style="top:297px"></div>
  <div class="abs address-line" style="top:348px"></div>

  <p class="abs payment-label">Acceptable Payment method</p>
  <div class="abs payment-row">
    <span class="pay-chip chip-a"></span>
    <span class="pay-chip chip-b"></span>
    <span class="pay-chip chip-c"></span>
    <span class="pay-chip chip-d"></span>
    <span class="pay-chip chip-e"></span>
    <span class="pay-chip chip-f"></span>
    <span class="pay-chip chip-g"></span>
  </div>
</section>

</body>
</html>
```